HUSH: Hush Until Stories Happen school library event

I need two poster designs for Hush Until Stories Happen (HUSH) in BC, requested by the PCSMG--Pacific Coast School Media Guild. One should be for elementary students and one for high school. I want the date (Monday, October 26, 2020) and Hush Until Stories Happen. I would like the posters in English and in French. French is : Ferme Ton Écran Maintenant! I'm including last year's posters as examples. I would like to be able to print the poster files on 11x17 paper.

• -The phrase "Hush Until Stories Happen" for the English version; "Ferme Ton Écran Maintenant" for the French version.
-Include the organization name: Pacific Coast School Media Guild
-The date: Monday, October 26, 2020
• I would like the elementary version to be bright and colourful--fun for younger kids. I would like the high school version to be a bit more mature for the older students. Can still be bright and colourful.

```html
<!DOCTYPE html>
<html lang="en">
<head>
<meta charset="utf-8">
<title>HUSH – Hush Until Stories Happen posters</title>
<link href="https://fonts.googleapis.com/css2?family=Anton&family=Kaushan+Script&display=swap" rel="stylesheet">
<style>
  :root{
    --stage:#03062b;
    --paper:#ffffff;
    --royal:#1a2fc4;
    --royal-deep:#1524a0;
    --royal-bright:#3048f0;
    --label-blue:#1f35b8;
    --amber:#f7a81b;
    --amber-dark:#d98d0c;
    --slate:#c0c9c9;
    --ink:#1d1d1d;
  }
  *{margin:0;padding:0;box-sizing:border-box}
  html,body{width:1200px;height:900px;overflow:hidden;background:var(--stage)}
  .stage{position:relative;width:1200px;height:900px;font-family:Arial,Helvetica,sans-serif}
  .poster{position:absolute;top:65px;width:499px;height:770px;overflow:hidden}
  .poster--elementary{left:80px;background:var(--paper)}
  .poster--secondary{left:622px;background:var(--royal)}

  .org-label{position:absolute;display:block;white-space:nowrap;font-size:21px;line-height:1;padding:7px 10px;text-align:center}
  .poster--elementary .org-label{background:var(--label-blue);color:#fff}
  .poster--secondary .org-label{background:var(--amber);color:var(--ink);font-size:24px;padding:8px 11px}

  .grid-cell{position:absolute;background:var(--slate)}
  .photo{position:absolute}

  .tagline{position:absolute;background:var(--amber);color:var(--ink);font-family:"Kaushan Script",cursive;white-space:nowrap;text-align:center}
  .poster--elementary .tagline{left:132px;top:527px;width:234px;height:44px;font-size:17px;line-height:44px;transform:rotate(-3deg)}

  .acronym{position:absolute;left:82px;top:578px;font-family:Anton,Impact,sans-serif;font-size:94px;line-height:1;color:var(--royal-bright);letter-spacing:4px;white-space:nowrap}
  .acronym .dot{color:var(--amber)}

  .event-date{position:absolute;font-size:16px;line-height:30px;height:30px;text-align:center;white-space:nowrap}
  .poster--elementary .event-date{left:147px;top:703px;width:205px;background:var(--slate);color:var(--ink)}
  .poster--secondary .event-date{left:147px;top:704px;width:205px;background:var(--royal-deep);color:#fff}

  .headline{position:absolute;left:0;top:0}
  .poster--secondary .tagline{left:58px;top:402px;width:368px;height:50px;font-size:25px;line-height:50px;transform:rotate(-7deg)}
</style>
</head>
<body>
<main class="stage">

  <section class="poster poster--elementary" aria-label="Elementary poster">
    <span class="org-label" style="left:111px;top:55px;width:276px">Pacific Coast School</span>
    <span class="org-label" style="left:123px;top:94px;width:252px">Media Guild</span>

    <div class="photo" role="img" aria-label="Photo of a young girl in glasses reading while seated on a stack of books" style="left:75px;top:167px;width:111px;height:219px;background:linear-gradient(180deg,#e4e4ee,#d9c59c 60%,#c9b08a)"></div>
    <div class="grid-cell" style="left:194px;top:167px;width:111px;height:107px"></div>
    <div class="photo" role="img" aria-label="Photo of a toddler reading a picture book on a sofa" style="left:312px;top:167px;width:111px;height:107px;background:linear-gradient(160deg,#e8e2d8,#c94a4a 60%,#8aa7b8)"></div>
    <div class="photo" role="img" aria-label="Photo of a boy lying on the floor reading by a sunny window" style="left:194px;top:279px;width:229px;height:107px;background:linear-gradient(180deg,#cfe0dc,#b9c7b8 55%,#e6dcc8)"></div>
    <div class="grid-cell" style="left:75px;top:391px;width:111px;height:107px"></div>
    <div class="photo" role="img" aria-label="Photo of a child in green glasses holding letter cards" style="left:194px;top:391px;width:111px;height:107px;background:linear-gradient(180deg,#5fd6c8,#7ddcd0 60%,#f0e9e0)"></div>
    <div class="grid-cell" style="left:312px;top:391px;width:111px;height:107px"></div>

    <p class="tagline">Hush Until Stories Happen</p>
    <h1 class="acronym">H<span class="dot">.</span>U<span class="dot">.</span>S<span class="dot">.</span>H<span class="dot">.</span></h1>
    <p class="event-date">Monday, October 26, 2020</p>
  </section>

  <section class="poster poster--secondary" aria-label="High school poster">
    <span class="org-label" style="left:97px;top:47px;width:304px">Pacific Coast School</span>
    <span class="org-label" style="left:111px;top:91px;width:277px">Media Guild</span>

    <svg class="headline" width="499" height="770" viewBox="0 0 499 770" aria-label="HUSH">
      <g font-family="Anton, Impact, sans-serif" font-size="300">
        <text x="56" y="408" textLength="392" lengthAdjust="spacingAndGlyphs" fill="#2d45e6">HU</text>
        <text x="46" y="400" textLength="392" lengthAdjust="spacingAndGlyphs" fill="#ffffff">HU</text>
        <text x="46" y="678" textLength="414" lengthAdjust="spacingAndGlyphs" fill="#2d45e6">SH</text>
        <text x="36" y="670" textLength="414" lengthAdjust="spacingAndGlyphs" fill="#ffffff">SH</text>
      </g>
      <polygon points="52,440 64,452 62,462" fill="var(--amber-dark)"/>
      <polygon points="420,398 410,412 428,402" fill="var(--amber-dark)"/>
    </svg>

    <p class="tagline">Hush Until Stories Happen</p>
    <p class="event-date">Monday, October 26, 2020</p>
  </section>

</main>
</body>
</html>
```